Cube truck ZPL derola 2018 12ft roofing company wraping

ZPL derola 2018 12 ft want something similar to the truck design you did.

needs to display all the same informations

Add alot of black since the cube is white

if possible put pictures of real pretigious houses faded in the background of the design

place a logo on the front of the cube but nothing on the doors or hood

```html
<!DOCTYPE html>
<html lang="fr">
<head>
<meta charset="utf-8">
<title>Les Toitures Altano Inc. – Vehicle Wrap</title>
<link href="https://fonts.googleapis.com/css2?family=Arimo:wght@700&family=Poppins:wght@500&display=swap" rel="stylesheet">
<style>
  :root {
    --page: #ffffff;
    --wrap-black: #070707;
    --brand-blue: #1fa6d6;
    --brand-blue-deep: #0e7fa8;
    --ink: #0b1a24;
    --white: #ffffff;
    --sky: #9fb6cc;
    --facade: #e4e6e8;
    --cedar: #c08552;
  }
  * { box-sizing: border-box; margin: 0; padding: 0; }
  html, body {
    width: 1200px; height: 675px; overflow: hidden;
    background: var(--page);
  }
  .canvas { position: relative; width: 1200px; height: 675px; }

  .wrap-panel {
    position: absolute; left: 84px; top: 172px;
    width: 1040px; height: 300px; overflow: hidden;
  }
  .house-photo {
    position: absolute; inset: 0;
    background:
      linear-gradient(180deg, rgba(255,255,255,0) 60%, rgba(150,120,90,0.35) 100%),
      linear-gradient(100deg, var(--sky) 0%, #c7d3de 45%, var(--facade) 70%, #d8cbbd 88%, var(--cedar) 100%);
  }
  .wrap-shapes { position: absolute; inset: 0; }

  .wrap-panel p, .wrap-panel li, .wrap-panel span { white-space: nowrap; }

  .brand-prefix {
    position: absolute; left: 225px; top: 138px;
    font-family: "Poppins", sans-serif; font-weight: 500;
    font-size: 27px; line-height: 1; color: var(--white);
  }
  .brand-main {
    position: absolute; left: 286px; top: 172px;
    font-family: "Poppins", sans-serif; font-weight: 500;
    font-size: 62px; line-height: 1; letter-spacing: 1px; color: var(--white);
  }
  .brand-suffix {
    position: absolute; left: 558px; top: 230px;
    font-family: "Poppins", sans-serif; font-weight: 500;
    font-size: 20px; line-height: 1; color: var(--white);
  }

  .service-list {
    position: absolute; left: 411px; top: 120px;
    list-style: none;
    font-family: "Arimo", sans-serif; font-weight: 700;
    font-size: 15px; line-height: 18px; color: var(--white);
  }

  .market-tagline {
    position: absolute; left: 465px; top: 18px; width: 160px;
    text-align: center;
    font-family: "Arimo", sans-serif; font-weight: 700;
    font-size: 19px; line-height: 23px;
  }
  .market-tagline .line-blue {
    display: block; color: var(--brand-blue-deep);
    -webkit-text-stroke: 1px var(--ink);
  }
  .market-tagline .line-white {
    display: block; color: var(--white);
    -webkit-text-stroke: 1px var(--ink);
  }

  .phone-number {
    position: absolute; left: 261px; top: 240px;
    font-family: "Arimo", sans-serif; font-weight: 700;
    font-size: 28px; line-height: 1; color: var(--ink);
  }
  .website {
    position: absolute; left: 392px; top: 274px;
    font-family: "Arimo", sans-serif; font-weight: 700;
    font-size: 16px; line-height: 1; color: var(--white);
  }
</style>
</head>
<body>
<main class="canvas">
  <section class="wrap-panel" aria-label="Side wrap design for Les Toitures Altano Inc.">
    <div class="house-photo" role="img" aria-label="Photo of a modern two-storey house with dark tiled roof, white stucco, cedar siding and a balcony under a cloudy blue sky"></div>

    <svg class="wrap-shapes" viewBox="0 0 1040 300" width="1040" height="300" aria-hidden="true">
      <polygon points="0,0 385,0 680,300 0,300" fill="var(--wrap-black)"/>
      <polygon points="385,0 400,0 695,300 680,300" fill="var(--brand-blue)"/>
      <polygon points="404,0 420,0 715,300 699,300" fill="var(--brand-blue-deep)"/>
      <polygon points="420,0 424,0 719,300 715,300" fill="var(--brand-blue)"/>
      <polygon points="216,238 448,238 470,268 216,268" fill="var(--brand-blue)"/>
    </svg>

    <div class="market-tagline">
      <span class="line-blue">RESIDENTIAL &amp;</span>
      <span class="line-white">COMMERCIAL</span>
    </div>

    <span class="brand-prefix">Les Toitures</span>
    <span class="brand-main">ALTANO</span>
    <span class="brand-suffix">Inc.</span>

    <ul class="service-list">
      <li>INSPECTION</li>
      <li>REPARATION</li>
      <li>REFECTION</li>
    </ul>

    <p class="phone-number">514-555-0182</p>
    <p class="website">www.toituresaltano.com</p>
  </section>
</main>
</body>
</html>
```